Creative Landscape Architecture Company Needs a Creative Business Card Design

Varn and Partners, Inc. is a landscape architecture (LA) company started in 1997 in Austin, TX. We work on large commerical projects all around the U.S. and provide land planning, site planning, landscape design and architectural renderings.

We don't want this card to look like a LA firm's business card. We are looking for a business card design that is edgy and cool to reflect the more artistic and creative side of our company. We would like our clients to think "now there's a business card unlike any other LA that I've seen before."

We would like it to be in standard 2"x3.5" format. Double sided. Full color ok. Our company logo is attached. We like the logo but would not be adverse to any variations you would like to make to it. Feel free to change it up. Typically the logo has been a light saturated orange color but its not necessary that you stick with it.

Landscape

Requirements
Must have
• 1. Company name
2. individuals name
3. email address
4. cell number
5. office number
6. website: www.varnandpartners.example
7. Business address
Nice to have
• Can add (but not necessary)
Personal titles such as "president" or "registered landscape architect"

```html
<!DOCTYPE html>
<html lang="en">
<head>
<meta charset="utf-8">
<title>Varn and Partners, Inc. — Business Card</title>
<link rel="stylesheet" href="https://fonts.googleapis.com/css2?family=Questrial&family=Source+Sans+3:wght@400&display=swap">
<style>
  :root {
    --sheet: #ffffff;
    --card: #000000;
    --leaf-light: #8dc63f;
    --leaf-dark: #4f7f24;
    --ink-light: #ffffff;
    --icon-grey: #8a8a8a;
    --label-ink: #111111;
    --edge: #6a8f2a;
  }
  html, body {
    margin: 0;
    padding: 0;
    width: 1200px;
    height: 939px;
    overflow: hidden;
    background: var(--sheet);
  }
  .sheet {
    position: relative;
    width: 1200px;
    height: 939px;
  }
  .card {
    position: absolute;
    width: 406px;
    height: 232px;
    background: var(--card);
    overflow: hidden;
    font-family: "Questrial", sans-serif;
    color: var(--ink-light);
  }
  .card--front { left: 143px; top: 171px; }
  .card--back-1 { left: 144px; top: 547px; outline: 1px solid var(--edge); }
  .card--back-2 { left: 688px; top: 547px; outline: 1px solid var(--edge); }

  .card__foliage {
    position: absolute;
    left: 0;
    top: 0;
    width: 245px;
    height: 232px;
  }

  .holder-name {
    position: absolute;
    left: 226px;
    top: 43px;
    font-size: 12.5px;
    letter-spacing: 0.1px;
  }
  .holder-title {
    position: absolute;
    right: 32px;
    top: 65px;
    font-size: 7px;
  }
  .contact {
    position: absolute;
    left: 226px;
    font-size: 10.5px;
    line-height: 14px;
  }
  .contact--address { top: 92px; }
  .contact--office { top: 134px; }
  .contact--mobile { top: 161px; }
  .contact--web { top: 188px; }

  .icon {
    position: absolute;
    left: 204px;
    fill: none;
    stroke: var(--icon-grey);
    stroke-width: 1.4;
  }
  .icon--mail { top: 99px; }
  .icon--phone { top: 132px; }
  .icon--mobile { top: 159px; }
  .icon--screen { top: 194px; }

  .brand-block {
    position: absolute;
    left: 163px;
    top: 53px;
    width: 81px;
    height: 126px;
    background: var(--leaf-light);
  }
  .brand-name {
    position: absolute;
    left: 255px;
    top: 167px;
    font-size: 12.5px;
    white-space: nowrap;
  }
  .brand-name--green { color: var(--leaf-light); }

  .sheet-label {
    position: absolute;
    font-family: "Source Sans 3", sans-serif;
    font-size: 21px;
    color: var(--label-ink);
    margin: 0;
    font-weight: 400;
  }
  .sheet-label--front { left: 157px; top: 442px; }
  .sheet-label--back-1 { left: 157px; top: 816px; }
  .sheet-label--back-2 { left: 699px; top: 816px; }
</style>
</head>
<body>
<main class="sheet">

  <section class="card card--front" aria-label="Front side of card">
    <svg class="card__foliage" viewBox="0 0 245 232" role="img" aria-label="Large green leaf illustration sweeping in from the left edge">
      <defs>
        <linearGradient id="foliage-tone" x1="0" y1="0" x2="1" y2="1">
          <stop offset="0" stop-color="var(--leaf-dark)"/>
          <stop offset="0.35" stop-color="var(--leaf-light)"/>
          <stop offset="1" stop-color="var(--leaf-light)"/>
        </linearGradient>
      </defs>
      <path d="M0 0 H235 C220 20 205 40 195 60 C175 75 170 95 160 110 C150 130 120 140 110 165 C100 185 105 205 100 232 H0 Z" fill="url(#foliage-tone)"/>
    </svg>

    <div class="holder-name">Fname Lname</div>
    <div class="holder-title">[ marketing director ]</div>

    <svg class="icon icon--mail" width="20" height="14" viewBox="0 0 20 14" aria-hidden="true">
      <rect x="1" y="1" width="18" height="12"/>
      <path d="M1 1 L10 8 L19 1 M1 13 L8 6.5 M19 13 L12 6.5"/>
    </svg>
    <div class="contact contact--address">4410 Cedar Bend, Suite 210<br>Austin, Texas 78701</div>

    <svg class="icon icon--phone" width="18" height="18" viewBox="0 0 18 18" aria-hidden="true">
      <rect x="1" y="2" width="4" height="15" rx="1"/>
      <rect x="6" y="3" width="11" height="14"/>
      <path d="M8 7 h7 M8 10 h7 M8 13 h7"/>
    </svg>
    <div class="contact contact--office">512.555.0148</div>

    <svg class="icon icon--mobile" width="18" height="20" viewBox="0 0 18 20" aria-hidden="true">
      <rect x="4" y="1" width="10" height="18" rx="2"/>
      <path d="M6 4 h6 v10 h-6 Z"/>
    </svg>
    <div class="contact contact--mobile">512 555 0193</div>

    <svg class="icon icon--screen" width="20" height="18" viewBox="0 0 20 18" aria-hidden="true">
      <rect x="1" y="1" width="18" height="11" rx="1"/>
      <path d="M8 12 L6 17 H14 L12 12"/>
    </svg>
    <div class="contact contact--web">mymail@varnandpartners.example<br>www.varnandpartners.example</div>
  </section>
  <p class="sheet-label sheet-label--front">FRONT SIDE</p>

  <section class="card card--back-1" aria-label="Back side, variation one">
    <div class="brand-block" aria-hidden="true"></div>
    <div class="brand-name">Varn and Partners, Inc.</div>
  </section>
  <p class="sheet-label sheet-label--back-1">BACK SIDE _ Var. 1</p>

  <section class="card card--back-2" aria-label="Back side, variation two">
    <div class="brand-block" aria-hidden="true"></div>
    <div class="brand-name brand-name--green">Varn and Partners, Inc.</div>
  </section>
  <p class="sheet-label sheet-label--back-2">BACK SIDE _ Var. 2</p>

</main>
</body>
</html>
```